Eastfield Commercial Card

I would like a modern, eye catching card based off my logo design.
Info to include:
Anders Voll (Card Name)
eastfieldcommercial.example (Website)
555 203 8841 (Office/fax)
555 287 3096 (Business Cell)
anders@eastfieldcommercial.example (Work email)

Target Market(s)

Commercial real estate brokers, property owners.

Colors
ec1f27
757575

Requirements
Must have
• Name and info above. Not be lame!:)

```html
<!DOCTYPE html>
<html lang="en">
<head>
<meta charset="utf-8">
<title>Eastfield Commercial Card</title>
<link rel="stylesheet" href="https://fonts.googleapis.com/css2?family=Montserrat:wght@700&family=Open+Sans:wght@400&display=swap">
<style>
  :root {
    --brand-red: #9c0a0a;
    --brand-grey: #4a4a4a;
    --card-white: #ffffff;
    --backdrop: #ecebe8;
    --ink: #333333;
  }
  html, body {
    margin: 0;
    width: 1200px;
    height: 900px;
    overflow: hidden;
    background: var(--backdrop);
  }
  .canvas {
    position: relative;
    width: 1200px;
    height: 900px;
  }
  .card {
    position: absolute;
    width: 560px;
    height: 320px;
    border-radius: 3px;
    box-shadow: 0 8px 24px rgba(0,0,0,0.18);
    overflow: hidden;
  }
  .card-back {
    left: 60px;
    top: 90px;
    background: var(--brand-red);
    display: flex;
    align-items: center;
    justify-content: center;
  }
  .card-back .brand-name {
    font-family: "Montserrat", sans-serif;
    font-weight: 700;
    font-size: 26px;
    letter-spacing: 1px;
    text-transform: uppercase;
    color: var(--card-white);
  }
  .card-front {
    left: 580px;
    top: 470px;
    background: var(--card-white);
  }
  .holder-name {
    position: absolute;
    left: 52px;
    top: 70px;
    margin: 0;
    font-family: "Montserrat", sans-serif;
    font-weight: 700;
    font-size: 19px;
    letter-spacing: 1.5px;
    text-transform: uppercase;
    color: var(--brand-red);
  }
  .brand-lockup {
    position: absolute;
    right: 34px;
    top: 58px;
    display: flex;
    align-items: center;
    gap: 10px;
  }
  .brand-mark {
    width: 16px;
    height: 16px;
    background: var(--brand-grey);
  }
  .brand-lockup .brand-name {
    font-family: "Montserrat", sans-serif;
    font-weight: 700;
    font-size: 16px;
    letter-spacing: 0.5px;
    text-transform: uppercase;
    color: var(--brand-red);
  }
  .contact-list {
    position: absolute;
    left: 52px;
    top: 140px;
    margin: 0;
    padding: 0;
    list-style: none;
    font-family: "Open Sans", sans-serif;
    font-size: 15px;
    line-height: 20px;
    color: var(--ink);
    z-index: 2;
  }
  .contact-list li {
    display: flex;
    align-items: center;
    gap: 8px;
  }
  .contact-list svg {
    width: 13px;
    height: 13px;
    fill: var(--brand-red);
    flex: none;
  }
  .wave {
    position: absolute;
    left: 0;
    top: 0;
    width: 560px;
    height: 320px;
  }
  .wave .band { fill: var(--brand-red); }
  .wave .swoosh { fill: var(--brand-grey); }
</style>
</head>
<body>
<main class="canvas">

  <section class="card card-back">
    <span class="brand-name">Eastfield Commercial</span>
  </section>

  <section class="card card-front">
    <svg class="wave" viewBox="0 0 560 320" aria-hidden="true">
      <path class="swoosh" d="M0 236 C120 282 320 258 470 178 C350 262 150 292 0 262 Z"/>
      <path class="band" d="M0 272 C170 300 380 252 560 150 L560 320 L0 320 Z"/>
    </svg>

    <h1 class="holder-name">Anders Voll</h1>

    <div class="brand-lockup">
      <span class="brand-mark"></span>
      <span class="brand-name">Eastfield Commercial</span>
    </div>

    <ul class="contact-list">
      <li>
        <svg viewBox="0 0 12 12"><path d="M3 0h6a1 1 0 0 1 1 1v10a1 1 0 0 1-1 1H3a1 1 0 0 1-1-1V1a1 1 0 0 1 1-1zm0 1.5v8h6v-8z"/></svg>
        <span>555 287 3096</span>
      </li>
      <li>
        <svg viewBox="0 0 12 12"><path d="M0 4c0-2 2-3 6-3s6 1 6 3v1H9V4H3v1H0zm2 2h8l1 5H1z"/></svg>
        <span>555 203 8841</span>
      </li>
      <li>
        <svg viewBox="0 0 12 12"><path d="M3 0h6v3H3zM0 4h12v5h-2v3H2V9H0zm3 4v3h6V8z"/></svg>
        <span>555 203 8841</span>
      </li>
      <li>
        <svg viewBox="0 0 12 12"><path d="M0 2h12v8H0zm1 1l5 4 5-4v-0.2H1z"/></svg>
        <span>anders@eastfieldcommercial.example</span>
      </li>
      <li>
        <svg viewBox="0 0 12 12"><circle cx="6" cy="6" r="6"/></svg>
        <span>www.eastfieldcommercial.example</span>
      </li>
    </ul>
  </section>

</main>
</body>
</html>
```